Digital Mapping company needs a Proposal Cover Page template (Not Cover Letter).

We are looking for a new design of our proposal's front page. Sales people at Brindle Surveys will use this new cover page when bidding for jobs, there will be Brindle Surveys elements that will be set in stone but the potential client information will need to be adaptable/customizable (for example, we currently upload client logos to the home page of our proposals). I attach what we currently have.
Similar look and feel as our tradeshow booth pull up banners and website (www.brindlesurveys-example.com) (images of these are also attached). We would like to see designs that use similar colours: green/blue/teal/yellow/orange/red.

We have clients all over the world. We own state of the art mapping equipment (LiDAR). LiDAR and digital photography are acquired with our own Volkar 318 and other aircraft. The final proposal design should be recognizable and communicate: an experienced company, high quality, and state of the art mapping technology delivered worldwide.

Target Market(s)

Our clients are global and range from small business to large corporations. We have clients associated with Mining, Forestry, Engineering, Ecological and First Nations sectors (usually hired by Geologists & Engineers)

Industry/Entity Type

Technical Service

Font styles to use
Serif

Colors

Designer to choose colors to be used in the design.

Requirements
Must have
• Here are the basic items we would like to see on the cover page of our proposal:
• Our Company Name - Brindle Surveys Ltd.
• Our Company Logo - attached
• Our Company contact information [customizable field as we have a few locations]
• Proposal service [customizable field to add]
• Proposal project name and location [customizable field to add]
• Proposal Job number [customizable field to add]
• Recipient company or individual and their logo [customizable field’s to add these]
• Date created [auto date]
• Subdued information/less focus on Brindle Surveys’s name and contact information and a greater focus on the client and their project. Well chosen imagery will tie Brindle Surveys’s services to the client’s needs without the client thinking about it. Good use of white space as well.
Nice to have
• Similar look and feel as our tradeshow booth pull up banners and website (images of these are attached). We would like to see designs that use similar colours: green/yellow/red/blue/teal.
Should not have
• Something that doesn't match or fit with our logo/website/pull up tradeshow banners that are attached. Something that doesn't include all the elements in our must have list.

```html
<!DOCTYPE html>
<html lang="en">
<head>
<meta charset="utf-8">
<title>Brindle Surveys – Proposal Template Pages</title>
<link rel="stylesheet" href="https://fonts.googleapis.com/css2?family=Poppins:wght@500;600;700&family=Lato:ital,wght@0,400;0,700;1,400&family=Merriweather:ital,wght@0,400;0,700;1,400&display=swap">
<style>
:root{
  --stage:#000;
  --paper:#fff;
  --teal:#1a93bf;
  --teal-dark:#0e7ea8;
  --ink:#2b2b2b;
  --body:#4a4a4a;
  --muted:#7a7a7a;
  --rule:#c9d6e0;
  --placeholder:#d0d0d0;
  --tone-light:#e6e6e6;
  --slot:#f1f3f4;
}
*{margin:0;padding:0;box-sizing:border-box}
html,body{width:1200px;height:839px;overflow:hidden;background:var(--stage)}
.board{position:relative;width:1200px;height:839px}
.sheet{position:absolute;width:282px;height:400px;background:var(--paper);overflow:hidden;font-family:"Lato",sans-serif;color:var(--body)}
.col-1{left:13px}.col-2{left:314px}.col-3{left:608px}.col-4{left:907px}
.row-1{top:13px}.row-2{top:427px}

.brand{position:absolute;right:10px;top:9px;display:flex;align-items:center;gap:3px;font-family:"Poppins",sans-serif;font-weight:600;font-size:6.4px;color:var(--ink);letter-spacing:.2px}
.brand-dot{width:8px;height:8px;border-radius:50%;background:var(--teal)}

.page-title{position:absolute;left:12px;top:9px;font-family:"Poppins",sans-serif;font-weight:600;font-size:11.5px;color:var(--teal)}
.page-title.is-small{font-size:6.6px;color:var(--ink);font-weight:500;top:14px}
.page-title.is-dark{color:var(--ink);font-weight:500;font-size:10.5px;top:11px}

.folio{position:absolute;left:8px;right:8px;bottom:14px;border-top:.7px solid var(--rule)}
.folio span{position:absolute;left:50%;top:3px;transform:translateX(-50%);font-size:4.6px;color:var(--teal)}

.heading{font-family:"Lato",sans-serif;font-weight:700;font-size:7.2px;color:var(--teal);margin-bottom:3px}
.copy{font-size:5.1px;line-height:1.66;color:var(--body)}
.copy + .copy{margin-top:6px}
.copy.is-accent{color:var(--teal);font-style:italic}
.block{position:absolute}
.two-col{display:grid;grid-template-columns:1fr 1fr;gap:10px}

/* cover */
.cover-terrain{position:absolute;left:0;top:0;width:282px;height:207px;
  background:radial-gradient(ellipse at 30% 10%,#c9a21a 0%,transparent 45%),radial-gradient(ellipse at 80% 30%,#a9b21a 0%,transparent 50%),linear-gradient(170deg,#b88d16 0%,#8fb21f 35%,#2fb536 70%,#19c23c 100%)}
.cover-band{position:absolute;left:0;top:207px;width:282px;height:31px;background:var(--teal);display:flex;align-items:center;justify-content:center;font-family:"Merriweather",serif;font-weight:700;font-size:11.5px;color:#fff}
.cover-band::after{content:"";position:absolute;left:50%;bottom:-10px;transform:translateX(-50%);border-left:11px solid transparent;border-right:11px solid transparent;border-top:10px solid var(--teal)}
.cover-client{position:absolute;left:24px;right:24px;top:258px;font-family:"Merriweather",serif}
.client-row{display:flex;align-items:center;gap:9px;padding-bottom:7px;border-bottom:.7px solid var(--rule)}
.client-logo{flex:0 0 34px;height:34px;background:var(--slot);border:.7px solid var(--rule)}
.client-label{font-size:4.6px;letter-spacing:.6px;text-transform:uppercase;color:var(--teal)}
.client-name{font-size:10px;font-weight:700;color:var(--ink);line-height:1.3}
.cover-facts{display:grid;grid-template-columns:1fr 1fr;gap:5px 12px;margin-top:7px}
.fact dt{font-size:4.4px;letter-spacing:.5px;text-transform:uppercase;color:var(--muted)}
.fact dd{font-size:5.8px;color:var(--ink);line-height:1.4}
.cover-footer{position:absolute;left:0;right:0;bottom:16px;text-align:center;font-family:"Merriweather",serif}
.cover-brand{display:flex;justify-content:center;align-items:center;gap:5px;font-size:8.5px;font-weight:700;color:var(--ink)}
.cover-brand .brand-dot{width:11px;height:11px}
.cover-contact{margin-top:4px;font-size:4.6px;color:var(--muted);line-height:1.6}

/* about */
.hero-art{position:absolute;left:0;top:32px;width:282px;height:136px;background:linear-gradient(135deg,#e3e3e3,#bdbdbd 60%,#9e9e9e)}

/* services */
.hero-placeholder{position:absolute;left:0;top:38px;width:282px;height:97px;background:var(--placeholder)}
.service-band{position:absolute;left:0;top:135px;width:282px;height:30px;background:var(--teal);color:#fff;padding:4px 12px}
.service-band h2{font-family:"Poppins",sans-serif;font-weight:600;font-size:10.5px;line-height:1.2}
.service-band p{font-family:"Poppins",sans-serif;font-size:4.2px;font-weight:600}
.service-band::after{content:"";position:absolute;left:18px;bottom:-7px;border-left:7px solid transparent;border-right:7px solid transparent;border-top:7px solid var(--teal)}
.service-list{position:absolute;left:25px;right:18px;top:204px;display:flex;flex-direction:column}
.service{display:flex;gap:9px;align-items:flex-start;height:44px}
.service-icon{flex:0 0 31px;height:31px;border-radius:50%;background:#1f1f1f;display:flex;align-items:center;justify-content:center}
.service h3{font-size:6.4px;font-weight:700;color:var(--teal);margin-bottom:1px}
.service .copy{font-size:4.9px;line-height:1.6}

/* image + text */
.image-slot{position:absolute;left:145px;width:122px;background:var(--placeholder)}

/* contents */
.toc{position:absolute;left:32px;right:34px;top:56px;list-style:none}
.toc li{display:flex;align-items:baseline;font-size:6.6px;color:var(--ink);height:19.5px}
.toc .dots{flex:1;border-bottom:.8px dotted #777;margin:0 4px;transform:translateY(-1px)}
.toc .num{width:14px;text-align:right}

/* tables */
.table-label{font-size:6.6px;font-weight:700;color:var(--teal);margin-bottom:4px}
.data{width:100%;border-collapse:collapse;font-size:4.4px;color:var(--ink)}
.data th{font-weight:700;text-align:left;height:12px;padding-left:5px}
.data td{height:10.6px;padding-left:5px}
.data td:not(:first-child),.data th:not(:first-child){width:36px}
.style-1 thead tr{border-bottom:.8px solid #8a8a8a}
.style-1{border-bottom:1.6px solid #b8c8d8}
.style-2 thead{background:var(--tone-light)}
.style-2 thead th{color:#555}
.style-3-wrap{border:.8px solid #c8d0d6}
.style-3 thead{background:var(--teal);color:#fff}
.style-3 th{color:#fff}
</style>
</head>
<body>
<main class="board">

  <!-- Cover -->
  <section class="sheet col-1 row-1">
    <div class="cover-terrain" role="img" aria-label="Aerial LiDAR elevation render of mountainous terrain, shaded from yellow to green"></div>
    <div class="cover-band">Project Title goes here</div>
    <div class="cover-client">
      <div class="client-row">
        <div class="client-logo" role="img" aria-label="Client logo placeholder"></div>
        <div>
          <p class="client-label">Prepared for</p>
          <p class="client-name">Client Company Name</p>
        </div>
      </div>
      <dl class="cover-facts">
        <div class="fact"><dt>Service</dt><dd>LiDAR &amp; Aerial Imagery</dd></div>
        <div class="fact"><dt>Location</dt><dd>Project Location, Region</dd></div>
        <div class="fact"><dt>Job Number</dt><dd>BS-0000-00</dd></div>
        <div class="fact"><dt>Date</dt><dd>DD Month YYYY</dd></div>
      </dl>
    </div>
    <div class="cover-footer">
      <div class="cover-brand"><span class="brand-dot"></span>Brindle Surveys Ltd.</div>
      <p class="cover-contact">Office Name · 000 Street Name, City · +1 000 000 0000<br>www.brindlesurveys-example.com</p>
    </div>
  </section>

  <!-- About -->
  <section class="sheet col-2 row-1">
    <h1 class="page-title">Business Title here</h1>
    <div class="brand"><span class="brand-dot"></span>Brindle Surveys</div>
    <div class="hero-art" role="img" aria-label="Grey desk illustration with an About Us document, laptop, coffee and team portraits"></div>
    <div class="block" style="left:12px;right:12px;top:183px">
      <h2 class="heading">Lorem ipsum dolor sit amet</h2>
      <div class="two-col">
        <div>
          <p class="copy">Lorem ipsum dolor sit amet, consectetur adipiscing elit, sed do eiusmod tempor incididunt ut labore et dolore magna aliqua. Ut enim ad minim veniam, quis nostrud exercitation ullamco laboris nisi ut aliquip ex ea commodo consequat. Duis aute irure dolor in reprehenderit in voluptate velit esse cillum dolore eu fugiat nulla pariatur. Excepteur sint occaecat cupidatat non proident, sunt in culpa qui officia deserunt mollit anim id est laborum."</p>
          <p class="copy">"Sed ut perspiciatis unde omnis iste natus error sit voluptatem accusantium doloremque laudantium, totam rem aperiam, eaque ipsa quae ab illo inventore veritatis et quasi architecto beatae vitae dicta sunt explicabo. Nemo enim ipsam voluptatem quia voluptas sit aspernatur aut odit aut fugit, sed quia consequuntur magni dolores eos qui ratione voluptatem sequi nesciunt. Neque porro quisquam est, qui</p>
        </div>
        <div>
          <p class="copy">"Lorem ipsum dolor sit amet, consectetur adipiscing elit, sed do eiusmod tempor incididunt ut labore et dolore magna aliqua. Ut enim ad minim veniam, quis nostrud exercitation ullamco laboris nisi ut aliquip ex ea commodo consequat. Duis aute irure dolor in reprehenderit in voluptate velit esse cillum dolore eu fugiat nulla pariatur. Excepteur sint occaecat cupidatat non proident, sunt in culpa qui officia deserunt mollit anim id est laborum."</p>
          <p class="copy">"Sed ut perspiciatis unde omnis iste natus error sit voluptatem accusantium doloremque laudantium, totam rem aperiam, eaque ipsa quae ab illo inventore veritatis et quasi architecto beatae vitae dicta sunt explicabo. Nemo enim ipsam voluptatem quia voluptas sit aspernatur aut odit aut fugit, sed quia consequuntur magni dolores eos qui ratione voluptatem sequi nesciunt. Neque porro</p>
        </div>
      </div>
    </div>
    <div class="folio"><span>01</span></div>
  </section>

  <!-- Services -->
  <section class="sheet col-3 row-1">
    <h1 class="page-title">Business Title here</h1>
    <div class="brand"><span class="brand-dot"></span>Brindle Surveys</div>
    <div class="hero-placeholder" role="img" aria-label="Image placeholder for services photograph"></div>
    <div class="service-band">
      <h2>OUR SERVICES</h2>
      <p>Project Subtitle goes here</p>
    </div>
    <h2 class="heading block" style="left:13px;top:183px">Lorem ipsum dolor sit amet</h2>
    <div class="service-list">
      <div class="service">
        <div class="service-icon"><svg width="14" height="14" viewBox="0 0 14 14" fill="none" stroke="#fff" stroke-width="1"><path d="M3 5a4.5 4.5 0 0 1 8 -1"/><path d="M11 1.5v2.5h-2.5"/><path d="M11 9a4.5 4.5 0 0 1 -8 1"/><path d="M3 12.5v-2.5h2.5"/></svg></div>
        <div><h3>Icon Title Here</h3><p class="copy">Lorem ipsum dolor sit amet, consectetur adipiscing elit, sed do eiusmod tempor incididunt ut labore et dolore magna aliqua. Ut enim ad minim veniam, quis nostrud exercitation ullamco laboris nisi ut aliquip voluptas nulla pariatur?"</p></div>
      </div>
      <div class="service">
        <div class="service-icon"><svg width="14" height="14" viewBox="0 0 14 14" fill="none" stroke="#fff" stroke-width="1"><rect x="3" y="2" width="8" height="10"/><path d="M5 5h4M5 7h4M5 9h3"/></svg></div>
        <div><h3>Icon Title Here</h3><p class="copy">Lorem ipsum dolor sit amet, consectetur adipiscing elit, sed do eiusmod tempor incididunt ut labore et dolore magna aliqua. Ut enim ad minim veniam, quis nostrud exercitation ullamco laboris nisi ut aliquip voluptas nulla pariatur?"</p></div>
      </div>
      <div class="service">
        <div class="service-icon"><svg width="14" height="14" viewBox="0 0 14 14" fill="none" stroke="#fff" stroke-width="1"><rect x="2" y="3" width="10" height="7"/><path d="M5 12h4M4 6h6"/></svg></div>
        <div><h3>Icon Title Here</h3><p class="copy">Lorem ipsum dolor sit amet, consectetur adipiscing elit, sed do eiusmod tempor incididunt ut labore et dolore magna aliqua. Ut enim ad minim veniam, quis nostrud exercitation ullamco laboris nisi ut aliquip voluptas nulla pariatur?"</p></div>
      </div>
      <div class="service">
        <div class="service-icon"><svg width="14" height="14" viewBox="0 0 14 14" fill="none" stroke="#fff" stroke-width="1"><circle cx="4" cy="5" r="1.5"/><circle cx="10" cy="5" r="1.5"/><circle cx="7" cy="4" r="1.5"/><path d="M2 12v-3h4v3M8 12v-3h4v3"/></svg></div>
        <div><h3>Icon Title Here</h3><p class="copy">Lorem ipsum dolor sit amet, consectetur adipiscing elit, sed do eiusmod tempor incididunt ut labore et dolore magna aliqua. Ut enim ad minim veniam, quis nostrud exercitation ullamco laboris nisi ut aliquip voluptas nulla pariatur?"</p></div>
      </div>
    </div>
    <div class="folio"><span>01</span></div>
  </section>

  <!-- Text page -->
  <section class="sheet col-4 row-1">
    <h1 class="page-title is-small">Business Title here</h1>
    <div class="brand"><span class="brand-dot"></span>Brindle Surveys</div>
    <div class="block" style="left:12px;right:12px;top:40px">
      <h2 class="heading">Lorem ipsum dolor sit amet</h2>
      <p class="copy">Lorem ipsum dolor sit amet, consectetur adipiscing elit, sed do eiusmod tempor incididunt ut labore et dolore magna aliqua. Ut enim ad minim veniam, quis nostrud exercitation ullamco laboris nisi ut aliquip ex ea commodo consequat. Duis aute irure dolor in reprehenderit in voluptate velit esse cillum dolore eu fugiat nulla pariatur. Excepteur sint occaecat cupidatat non proident, sunt in culpa qui officia deserunt mollit anim id est laborum." Sed ut perspiciatis unde omnis iste natus error sit voluptatem accusantium doloremque laudantium, totam rem aperiam, eaque ipsa quae ab illo inventore veritatis et quasi architecto beatae vitae dicta sunt explicabo.</p>
      <p class="copy is-accent" style="margin-top:8px">Ut enim ad minima veniam, quis nostrum exercitationem ullam corporis suscipit laboriosam, nisi ut aliquid ex ea commodi consequatur? Quis autem vel eum iure reprehenderit qui in ea voluptate velit esse quam nihil molestiae consequatur, vel illum qui dolorem eum fugiat quo voluptas nulla pariatur?"</p>
    </div>
    <div class="block" style="left:12px;right:12px;top:165px">
      <h2 class="heading">Lorem ipsum dolor sit amet</h2>
      <div class="two-col">
        <div>
          <p class="copy">Lorem ipsum dolor sit amet, consectetur adipiscing elit, sed do eiusmod tempor incididunt ut labore et dolore magna aliqua. Ut enim ad minim veniam, quis nostrud exercitation ullamco laboris nisi ut aliquip ex ea commodo consequat. Duis aute irure dolor in reprehenderit in voluptate velit esse cillum dolore eu fugiat nulla pariatur. Excepteur sint occaecat cupidatat non proident, sunt in culpa qui officia deserunt mollit anim id est laborum."</p>
          <p class="copy">"Sed ut perspiciatis unde omnis iste natus error sit voluptatem accusantium doloremque laudantium, totam rem aperiam, eaque ipsa quae ab illo inventore veritatis et quasi architecto beatae vitae dicta sunt explicabo. Nemo enim ipsam voluptatem quia voluptas sit aspernatur aut odit aut fugit, sed quia consequuntur magni dolores eos qui ratione voluptatem sequi nesciunt. Neque porro quisquam est, qui dolorem ipsum quia dolor sit amet.</p>
        </div>
        <div>
          <p class="copy">"Lorem ipsum dolor sit amet, consectetur adipiscing elit, sed do eiusmod tempor incididunt ut labore et dolore magna aliqua. Ut enim ad minim veniam, quis nostrud exercitation ullamco laboris nisi ut aliquip ex ea commodo consequat. Duis aute irure dolor in reprehenderit in voluptate velit esse cillum dolore eu fugiat nulla pariatur. Excepteur sint occaecat cupidatat non proident, sunt in culpa qui officia deserunt mollit anim id est laborum."</p>
          <p class="copy">"Sed ut perspiciatis unde omnis iste natus error sit voluptatem accusantium doloremque laudantium, totam rem aperiam, eaque ipsa quae ab illo inventore veritatis et quasi architecto beatae vitae dicta sunt explicabo. Nemo enim ipsam voluptatem quia voluptas sit aspernatur aut odit aut fugit, sed quia consequuntur magni dolores eos qui ratione voluptatem sequi nesciunt. Neque porro quisquam est, qui dolorem ipsum.</p>
        </div>
      </div>
    </div>
    <div class="folio"><span>01</span></div>
  </section>

  <!-- Image + text page -->
  <section class="sheet col-1 row-2">
    <h1 class="page-title is-small">Business Title here</h1>
    <div class="brand"><span class="brand-dot"></span>Brindle Surveys</div>
    <div class="block" style="left:14px;width:122px;top:42px">
      <h2 class="heading">Lorem ipsum dolor sit amet</h2>
      <p class="copy">Lorem ipsum dolor sit amet, consectetur adipiscing elit, sed do eiusmod tempor incididunt ut labore et dolore magna aliqua. Ut enim ad minim veniam, quis nostrud exercitation ullamco laboris nisi ut aliquip ex ea commodo consequat. Duis aute irure dolor in reprehenderit in voluptate velit esse cillum dolore eu fugiat nulla pariatur. Excepteur sint occaecat cupidatat non proident, sunt in culpa qui officia deserunt mollit anim id est laborum. updatat non proident, sunt in culpa qui officia deserunt mollit anim id est laborum. nim id est laborum.</p>
    </div>
    <div class="image-slot" style="top:43px;height:119px" role="img" aria-label="Image placeholder"></div>
    <div class="block" style="left:14px;width:122px;top:209px">
      <h2 class="heading">Lorem ipsum dolor sit amet</h2>
      <p class="copy">Lorem ipsum dolor sit amet, consectetur adipiscing elit, sed do eiusmod tempor incididunt ut labore et dolore magna aliqua. Ut enim ad minim veniam, quis nostrud exercitation ullamco laboris nisi ut aliquip ex ea commodo consequat. Duis aute irure dolor in reprehenderit in voluptate velit esse cillum dolore eu fugiat nulla pariatur. Excepteur sint occaecat cupidatat non proident, sunt in culpa qui officia deserunt mollit anim id est laborum. updatat non proident, sunt in culpa qui officia deserunt mollit anim id est laborum.</p>
    </div>
    <div class="image-slot" style="top:210px;height:119px" role="img" aria-label="Image placeholder"></div>
    <div class="folio"><span>01</span></div>
  </section>

  <!-- Contents -->
  <section class="sheet col-2 row-2">
    <h1 class="page-title is-dark">Table Contents</h1>
    <div class="brand"><span class="brand-dot"></span>Brindle Surveys</div>
    <ol class="toc">
      <li>Table of Content<span class="dots"></span><span class="num">01</span></li>
      <li>About US<span class="dots"></span><span class="num">01</span></li>
      <li>Out Graphs<span class="dots"></span><span class="num">01</span></li>
      <li>Table of Content<span class="dots"></span><span class="num">01</span></li>
      <li>Table of Content<span class="dots"></span><span class="num">01</span></li>
      <li>Table of Content<span class="dots"></span><span class="num">01</span></li>
      <li>Table of Content<span class="dots"></span><span class="num">01</span></li>
      <li>Table of Content<span class="dots"></span><span class="num">01</span></li>
      <li>Table of Content<span class="dots"></span><span class="num">01</span></li>
      <li>Table of Content<span class="dots"></span><span class="num">01</span></li>
      <li>Table of Content<span class="dots"></span><span class="num">01</span></li>
      <li>Table of Content<span class="dots"></span><span class="num">01</span></li>
      <li>Table of Content<span class="dots"></span><span class="num">01</span></li>
    </ol>
    <div class="folio"><span>01</span></div>
  </section>

  <!-- Tables -->
  <section class="sheet col-3 row-2">
    <h1 class="page-title is-small">Business Title here</h1>
    <div class="brand"><span class="brand-dot"></span>Brindle Surveys</div>
    <div class="block" style="left:12px;right:14px;top:40px">
      <h2 class="heading">Lorem ipsum dolor sit amet</h2>
      <p class="copy">Lorem ipsum dolor sit amet, consectetur adipiscing elit, sed do eiusmod tempor incididunt ut labore et dolore magna aliqua. Ut enim ad minim veniam, quis nostrud exercitation ullamco laboris nisi ut aliquip ex ea commodo consequat. Duis aute irure dolor in reprehenderit in voluptate velit esse cillum dolore eu fugiat nulla pariatur. Excepteur sint occaecat cupidatat non proident, sunt in culpa qui officia deserunt mollit anim id est laborum.</p>
    </div>
    <div class="block" style="left:12px;right:14px;top:104px">
      <h3 class="table-label">Table Style 1</h3>
      <table class="data style-1">
        <thead><tr><th>Title 1</th><th>Title 2</th><th>Title 3</th><th>Title 4</th><th>Title 5</th><th>Title 6</th></tr></thead>
        <tbody>
          <tr><td>Lorem ipsum dolor</td><td>xxx</td><td>xxx</td><td>xxx</td><td>xxx</td><td>xxx</td></tr>
          <tr><td>Lorem ipsum dolor</td><td>xxx</td><td>xxx</td><td>xxx</td><td>xxx</td><td>xxx</td></tr>
          <tr><td>Lorem ipsum dolor</td><td>xxx</td><td>xxx</td><td>xxx</td><td>xxx</td><td>xxx</td></tr>
          <tr><td>Lorem ipsum dolor</td><td>xxx</td><td>xxx</td><td>xxx</td><td>xxx</td><td>xxx</td></tr>
        </tbody>
      </table>
    </div>
    <div class="block" style="left:12px;right:14px;top:191px">
      <h3 class="table-label">Table Style 2</h3>
      <table class="data style-2">
        <thead><tr><th>Title 1</th><th>Title 2</th><th>Title 3</th><th>Title 4</th><th>Title 5</th><th>Title 6</th></tr></thead>
        <tbody>
          <tr><td>Lorem ipsum dolor</td><td>xxx</td><td>xxx</td><td>xxx</td><td>xxx</td><td>xxx</td></tr>
          <tr><td>Lorem ipsum dolor</td><td>xxx</td><td>xxx</td><td>xxx</td><td>xxx</td><td>xxx</td></tr>
          <tr><td>Lorem ipsum dolor</td><td>xxx</td><td>xxx</td><td>xxx</td><td>xxx</td><td>xxx</td></tr>
          <tr><td>Lorem ipsum dolor</td><td>xxx</td><td>xxx</td><td>xxx</td><td>xxx</td><td>xxx</td></tr>
        </tbody>
      </table>
    </div>
    <div class="block" style="left:12px;right:14px;top:274px">
      <h3 class="table-label">Table Style 3</h3>
      <div class="style-3-wrap">
        <table class="data style-3">
          <thead><tr><th>Title 1</th><th>Title 2</th><th>Title 3</th><th>Title 4</th><th>Title 5</th><th>Title 6</th></tr></thead>
          <tbody>
            <tr><td>Lorem ipsum dolor</td><td>xxx</td><td>xxx</td><td>xxx</td><td>xxx</td><td>xxx</td></tr>
            <tr><td>Lorem ipsum dolor</td><td>xxx</td><td>xxx</td><td>xxx</td><td>xxx</td><td>xxx</td></tr>
            <tr><td>Lorem ipsum dolor</td><td>xxx</td><td>xxx</td><td>xxx</td><td>xxx</td><td>xxx</td></tr>
            <tr><td>Lorem ipsum dolor</td><td>xxx</td><td>xxx</td><td>xxx</td><td>xxx</td><td>xxx</td></tr>
          </tbody>
        </table>
      </div>
    </div>
    <div class="folio"><span>01</span></div>
  </section>

  <!-- Graphs -->
  <section class="sheet col-4 row-2">
    <h1 class="page-title is-small">Business Title here</h1>
    <div class="brand"><span class="brand-dot"></span>Brindle Surveys</div>
    <div class="block" style="left:12px;right:14px;top:40px">
      <h2 class="heading">Lorem ipsum dolor sit amet</h2>
      <p class="copy">Lorem ipsum dolor sit amet, consectetur adipiscing elit, sed do eiusmod tempor incididunt ut labore et dolore magna aliqua. Ut enim ad minim veniam, quis nostrud exercitation ullamco laboris nisi ut aliquip ex ea commodo consequat. Duis aute irure dolor in reprehenderit in voluptate velit esse cillum dolore eu fugiat nulla pariatur. Excepteur sint occaecat cupidatat non proident, sunt in culpa qui officia deserunt mollit anim id est laborum.</p>
      <h2 class="heading" style="margin-top:7px">Graphs Title here</h2>
      <p class="copy">Lorem ipsum dolor sit amet, consectetur adipiscing elit, sed do eiusmod tempor incididunt ut labore et dolore magna aliqua. Ut enim ad minim veniam sed do eiusmod tempor</p>
    </div>
    <svg class="block" style="left:0;top:138px" width="282" height="80" viewBox="0 0 342 97" role="img" aria-label="Bar chart with three groups of three bars">
      <g fill="#1590b8"><rect x="37" y="43" width="22" height="42"/><rect x="67" y="29" width="22" height="56"/><rect x="97" y="50" width="22" height="35"/></g>
      <g fill="#5ab4ee"><rect x="146" y="52" width="20" height="33"/><rect x="169" y="29" width="19" height="56"/><rect x="192" y="71" width="19" height="14"/></g>
      <g fill="#5f5f5f"><rect x="236" y="41" width="19" height="44"/><rect x="259" y="13" width="19" height="72"/><rect x="282" y="77" width="18" height="8"/></g>
    </svg>
    <div class="block" style="left:12px;right:14px;top:218px">
      <h2 class="heading">PIE chart Title here</h2>
      <p class="copy">Lorem ipsum dolor sit amet, consectetur adipiscing elit, sed do eiusmod tempor incididunt ut labore et dolore magna aliqua. Ut enim ad minim veniam sed do eiusmod tempor</p>
    </div>
    <svg class="block" style="left:0;top:250px" width="282" height="122" viewBox="0 300 342 148" role="img" aria-label="Line chart with four series">
      <g stroke="#dcdcdc" stroke-width=".8">
        <path d="M70 310H278M70 327H278M70 344H278M70 361H278M70 378H278M70 395H278M70 412H278M70 432H278"/>
        <path d="M70 305V432M90 305V432M110 305V432M130 305V432M150 305V432M170 305V432M190 305V432M210 305V432M230 305V432M250 305V432M270 305V432"/>
      </g>
      <g fill="none" stroke-width="1.4">
        <path d="M70 432C85 380 100 345 120 343S170 330 190 331S225 342 260 370" stroke="#0b4f96"/>
        <path d="M70 432C85 400 100 370 120 364S170 345 190 343S230 345 260 343" stroke="#1b78c8"/>
        <path d="M70 432C88 410 100 385 120 377S170 364 190 360S230 365 260 335" stroke="#5ab4ee"/>
        <path d="M70 432C88 415 100 395 120 388S170 370 190 380S230 420 260 398" stroke="#9a9a9a"/>
        <path d="M70 432C90 420 105 398 120 398S160 410 190 412S230 380 260 325" stroke="#8fcff5"/>
      </g>
      <g>
        <circle cx="120" cy="343" r="2.4" fill="#0b4f96"/><circle cx="190" cy="331" r="2.4" fill="#0b4f96"/><circle cx="260" cy="370" r="2.4" fill="#0b4f96"/>
        <circle cx="120" cy="364" r="2.4" fill="#1b78c8"/><circle cx="190" cy="343" r="2.4" fill="#1b78c8"/><circle cx="260" cy="343" r="2.4" fill="#1b78c8"/>
        <circle cx="120" cy="377" r="2.4" fill="#5ab4ee"/><circle cx="190" cy="360" r="2.4" fill="#5ab4ee"/><circle cx="260" cy="335" r="2.4" fill="#5ab4ee"/>
        <circle cx="120" cy="388" r="2.4" fill="#9a9a9a"/><circle cx="190" cy="380" r="2.4" fill="#9a9a9a"/><circle cx="260" cy="398" r="2.4" fill="#9a9a9a"/>
        <circle cx="120" cy="398" r="2.4" fill="#8fcff5"/><circle cx="190" cy="412" r="2.4" fill="#8fcff5"/><circle cx="260" cy="325" r="2.4" fill="#8fcff5"/>
        <circle cx="70" cy="432" r="2.6" fill="#0b4f96"/>
      </g>
    </svg>
    <div class="folio"><span>01</span></div>
  </section>

</main>
</body>
</html>
```